Amber Hollow Productions

I need a business card design for a new freelance film production company using or incorporating the logo:
I want the card to be creative, minimal, yet professional. Feel free to use a variety of different shapes and sizes/ textures for the card.

Industry/Entity Type

Film Production

```html
<!DOCTYPE html>
<html lang="en">
<head>
<meta charset="utf-8">
<title>Amber Hollow Productions – Business Card</title>
<link rel="stylesheet" href="https://fonts.googleapis.com/css2?family=Open+Sans:wght@400;600&display=swap">
<style>
  :root {
    --brand-blue: #3d5aa8;
    --brand-blue-deep: #2b3f86;
    --card-white: #f1f1f2;
    --skyline-grey: #e2e2e4;
    --charcoal: #3a3a3c;
    --text-grey: #555558;
    --rule-grey: #9a9a9c;
    --page: #ffffff;
  }
  * { margin: 0; padding: 0; box-sizing: border-box; }
  html, body { width: 1200px; height: 1000px; overflow: hidden; background: var(--page); }
  body { position: relative; font-family: "Open Sans", Arial, sans-serif; }

  .header-band {
    position: absolute; left: 204px; top: 20px; width: 822px; height: 27px;
    background: var(--brand-blue);
  }

  .card { position: absolute; top: 123px; height: 140px; overflow: hidden; }

  /* Front */
  .card-front { left: 324px; width: 251px; background: var(--card-white); }
  .front-skyline {
    position: absolute; right: 0; top: 0; width: 150px; height: 134px;
    background: linear-gradient(160deg, var(--skyline-grey), #ececee 70%, var(--card-white));
  }
  .front-name {
    position: absolute; left: 34px; top: 52px; width: 80px;
    color: var(--brand-blue); font-weight: 600; font-size: 13px; line-height: 14px;
    text-transform: uppercase; text-align: center;
  }
  .front-name small { display: block; font-size: 5.5px; letter-spacing: 1.6px; line-height: 10px; }
  .contact {
    position: absolute; left: 124px; top: 56px;
    font-size: 6px; line-height: 8px; letter-spacing: 1px; color: var(--text-grey); font-weight: 600;
  }
  .contact .person { color: var(--brand-blue); }
  .contact .role { font-style: normal; margin-bottom: 7px; }
  .front-stripe { position: absolute; left: 0; bottom: 0; width: 100%; height: 5px; display: flex; }
  .front-stripe .blue { width: 112px; background: var(--brand-blue); }
  .front-stripe .dark { flex: 1; background: var(--charcoal); }

  /* Back */
  .card-back { left: 603px; width: 250px; background: var(--brand-blue); }
  .perforations { position: absolute; left: 17px; display: flex; gap: 9px; }
  .perforations.top { top: 9px; }
  .perforations.bottom { top: 122px; }
  .perforations span { width: 10px; height: 7px; background: var(--brand-blue-deep); }
  .back-name {
    position: absolute; left: 0; top: 52px; width: 100%;
    color: var(--brand-blue-deep); font-weight: 600; font-size: 13px; line-height: 14px;
    text-transform: uppercase; text-align: center;
  }
  .back-name small { display: block; font-size: 5.5px; letter-spacing: 1.6px; line-height: 10px; }

  .callouts { position: absolute; left: 0; top: 0; }
  .label { position: absolute; top: 309px; font-size: 9px; color: var(--charcoal); font-weight: 600; white-space: nowrap; }
</style>
</head>
<body>
  <div class="header-band"></div>

  <section class="card card-front">
    <div class="front-skyline" role="img" aria-label="Faint grey city skyline illustration"></div>
    <div class="front-name">Amber Hollow<small>Productions</small></div>
    <div class="contact">
      <p class="person">Dana Whitfield</p>
      <p class="role">Photographer</p>
      <p>+60 12 555 0184</p>
      <p>www.amberhollow.com</p>
      <p>info@amberhollow.com</p>
    </div>
    <div class="front-stripe"><span class="blue"></span><span class="dark"></span></div>
  </section>

  <section class="card card-back">
    <div class="perforations top"><span></span><span></span><span></span><span></span><span></span><span></span><span></span><span></span><span></span><span></span><span></span></div>
    <div class="back-name">Amber Hollow<small>Productions</small></div>
    <div class="perforations bottom"><span></span><span></span><span></span><span></span><span></span><span></span><span></span><span></span><span></span><span></span><span></span></div>
  </section>

  <svg class="callouts" width="1200" height="1000" aria-hidden="true">
    <g fill="none" stroke="var(--rule-grey)" stroke-width="1">
      <path d="M324.5 266v5h250v-5M448.5 271v32"/>
      <path d="M645.5 136v167M625.5 249v54"/>
      <path d="M730 184.5h136.5v118"/>
    </g>
    <g fill="var(--rule-grey)">
      <circle cx="645.5" cy="136" r="1.5"/>
      <circle cx="625.5" cy="249" r="1.5"/>
      <circle cx="730" cy="184.5" r="1.5"/>
    </g>
  </svg>

  <p class="label" style="left:432px">Printing</p>
  <p class="label" style="left:600px">Printing + Spot UV</p>
  <p class="label" style="left:830px">Printing + Spot UV</p>
</body>
</html>
```